Label Design DormaLux Capsules

Hello dear designers!

We run a brand for dietary supplements and are looking for a talented designer to help take our brand to the next level. We are planning to launch new products with fresh packaging and redesigned labels. Additionally, we would like to refresh our company logo to make it fit better on the packaging.

Important Info:

Our brand: PuraVeta – specializing in products for detoxification, sleep, and eye protection.
Our shop: www.puraveta-shop.at – currently offering two main products:
PuraVeta (Detox Tincture)
Ocula Shield Guard (Blue Light Filter Glasses)
Project Goal: Initially, we are looking for a label design for our new product DormaLux (sleep capsules). If we like the design, we would like to revise the label for our first product, PuraVeta, and potentially rework our logo to make it more compact and visually appealing on our packaging.

Design Preferences: We are fans of the design style of Varo Nutra and would love a design in a similar style – modern, clean, and premium – but with a unique touch that fits our brand. You will find some inspirations and ideas that we particularly like in the attachment.

Important:

Our packaging for DormaLux is an 8 OZ jar (similar to the smaller jars used by Varo Nutra).
The label should be clear, appealing, and give the product a high-quality look.
An example of a previous design draft (which hasn’t fully convinced us yet), along with inspirations for our upcoming bundle (including PuraVeta, DormaLux, and OculaShield Guard), is also attached.
Special Opportunity: The designer with the best concept will have the chance to collaborate with us long-term! We have two more brands in the pipeline and are looking for a reliable and creative partner for future projects. Generous compensation and tips are guaranteed.

We look forward to seeing creative and professional designs that will take our brand to the next level!

Target Market(s)

Germany

Industry/Entity Type

Supplement

Font styles to use
Sans Serif

Colors

Designer to choose colors to be used in the design.

Requirements
Must have
• Es sollte Hochwertig und Modern aussehen. Matt schwarzer hintergrund. less is more
Nice to have
• Maybe The head should be visible in the background.
Should not have
• it should not be colorful, and not too playful, it should definitely not look cheap!

```html
<!DOCTYPE html>
<html lang="de">
<head>
<meta charset="utf-8">
<title>DormaLux – Etikett</title>
<link rel="stylesheet" href="https://fonts.googleapis.com/css2?family=Oswald:wght@300;400&family=Montserrat:wght@500&display=swap">
<style>
  :root {
    --stage: #e4e4e4;
    --label-dark: #161718;
    --label-mid: #2c2e2f;
    --gold-light: #f1e4c6;
    --gold: #c9a46a;
    --gold-deep: #8d6a3a;
    --text-light: #f2f2f2;
    --hex-tint: rgba(40, 90, 105, 0.35);
  }
  * { margin: 0; padding: 0; box-sizing: border-box; }
  html, body { width: 1200px; height: 900px; overflow: hidden; }
  body { background: var(--stage); position: relative; font-family: "Oswald", sans-serif; }

  .label {
    position: absolute; left: 294px; top: 80px; width: 612px; height: 740px;
    background: radial-gradient(ellipse at 50% 35%, var(--label-mid) 0%, var(--label-dark) 75%);
    overflow: hidden;
  }
  .texture {
    position: absolute; left: 60px; top: 380px; width: 500px; height: 360px;
    background: radial-gradient(ellipse at 50% 35%, var(--hex-tint) 0%, rgba(60,60,60,0.25) 45%, transparent 75%);
  }
  .brand {
    position: absolute; top: 128px; left: 0; width: 100%; text-align: center;
    font-family: "Montserrat", sans-serif; font-weight: 500; color: var(--gold);
  }
  .brand-name { font-size: 25px; letter-spacing: 5px; display: block; }
  .brand-sub { font-size: 13px; letter-spacing: 5px; display: block; margin-top: 4px; }
  .product-title {
    position: absolute; left: 64px; top: 262px;
    font-weight: 400; font-size: 150px; line-height: 1; letter-spacing: 0;
    white-space: nowrap;
    transform: scaleX(0.75); transform-origin: left top;
    background: linear-gradient(180deg, var(--gold-light) 0%, var(--gold) 55%, var(--gold-deep) 100%);
    -webkit-background-clip: text; background-clip: text; color: transparent;
  }
  .claim { position: absolute; left: 66px; top: 416px; width: 396px; height: 56px; }
  .claim-text {
    position: absolute; left: 80px; top: 428px;
    font-size: 27px; font-weight: 400; color: var(--text-light); letter-spacing: 0.3px;
    white-space: nowrap;
  }
  .subheading {
    position: absolute; left: 0; width: 600px; top: 606px; text-align: center;
    font-size: 21px; color: var(--text-light);
  }
  .divider { position: absolute; left: 183px; top: 674px; width: 238px; height: 6px; }
  .contents {
    position: absolute; left: 0; width: 600px; top: 694px; text-align: center;
    font-size: 17px; font-weight: 300; color: var(--text-light); word-spacing: 2px;
  }
  .contents span + span { margin-left: 22px; }
</style>
</head>
<body>
  <main class="label">
    <div class="texture" role="img" aria-label="Dezentes Wabenmuster im Hintergrund"></div>

    <div class="brand">
      <span class="brand-name">PURAVETA</span>
      <span class="brand-sub">LUCENT OPTIK</span>
    </div>

    <h1 class="product-title">DORMALUX</h1>

    <svg class="claim" viewBox="0 0 396 56" aria-hidden="true">
      <defs>
        <linearGradient id="claimGold" x1="0" x2="1">
          <stop offset="0" stop-color="#f1e4c6"/>
          <stop offset="1" stop-color="#c9a46a"/>
        </linearGradient>
      </defs>
      <path d="M8 3 H394 L362 53 H8 Q3 53 3 48 V8 Q3 3 8 3 Z" fill="#1c1d1e" stroke="url(#claimGold)" stroke-width="2.5"/>
    </svg>
    <p class="claim-text">FÖRDERT DIE TIEFSCHLAFPHASE</p>

    <p class="subheading">ZWISCHENUBERSCRIFT HINZUFUGEN</p>

    <svg class="divider" viewBox="0 0 238 6" aria-hidden="true">
      <line x1="0" y1="3" x2="238" y2="3" stroke="#e8e8e8" stroke-width="5" stroke-dasharray="1.5 3" transform="skewX(-30)"/>
    </svg>

    <p class="contents"><span>30 PORTIONEN</span><span>60 KAPSELN</span></p>
  </main>
</body>
</html>
```